Educational Agency in Abu Dhabi looking for an 8 pages website

We are looking for an 8 pages design for a website, we already have one but we need to refine it and it is www.korvalendi.ae - Please base it on logo colours (attached) I have uploaded our logo, website content logo colors to use it for the scheme.
We are looking for a smooth look and content added if possible, I also attached content and logo

Industry/Entity Type

Education

Coding

Coded - Design and coding required

Number of Pages Required

5+ page

```html
<!DOCTYPE html>
<html lang="en">
<head>
<meta charset="utf-8">
<title>Korvalendi – Study Abroad</title>
<link href="https://fonts.googleapis.com/css2?family=Roboto:wght@400;500;700&display=swap" rel="stylesheet">
<style>
:root{
  --navy:#1f3567;
  --navy-dark:#172a55;
  --ink:#222;
  --muted:#555;
  --light:#f2f2f2;
  --footer:#1d1d1d;
  --white:#fff;
  --line:#dcdcdc;
}
*{box-sizing:border-box;margin:0;padding:0}
html,body{width:1200px;height:3982px;overflow:hidden}
body{font-family:"Roboto",Arial,sans-serif;color:var(--ink);background:var(--white);position:relative}
.abs{position:absolute}
/* header */
.topbar{position:absolute;left:0;top:0;width:1200px;height:117px;background:var(--white)}
.brand{position:absolute;left:66px;top:36px;display:flex;align-items:center;gap:12px;font-weight:700;font-size:26px;color:var(--navy)}
.brand .mark{width:40px;height:40px;background:var(--navy)}
.contact-item{position:absolute;top:36px;display:flex;align-items:center;gap:12px;font-size:13px;line-height:18px;color:var(--ink)}
.contact-item small{display:block;font-size:11px;color:var(--muted)}
.btn-apply{position:absolute;left:964px;top:35px;width:154px;height:39px;border-radius:20px;background:var(--navy);color:var(--white);font-size:13px;font-weight:700;display:flex;align-items:center;justify-content:center}
.nav{position:absolute;left:0;top:117px;width:1200px;height:53px;background:var(--navy);display:flex;align-items:center;padding-left:69px}
.nav a{color:var(--white);font-size:13px;text-decoration:none;padding:0 18px;height:53px;display:flex;align-items:center}
.nav a.active{background:var(--navy-dark)}
/* hero */
.hero{position:absolute;left:0;top:170px;width:1200px;height:573px;background:linear-gradient(90deg,#6f7d6a,#c9b9a3 40%,#b6b8b5 60%,#6d7a73)}
.hero h1{position:absolute;left:0;width:1200px;top:288px;text-align:center;color:var(--white);font-size:26px;font-weight:500;line-height:34px}
.hero .arrow{position:absolute;top:288px;width:28px;height:28px;border-radius:50%;background:var(--white);display:flex;align-items:center;justify-content:center}
.stats{position:absolute;left:297px;top:446px;width:606px;height:122px;background:rgba(31,53,103,.85);display:flex}
.stat{flex:1;display:flex;flex-direction:column;align-items:center;justify-content:center;color:var(--white);border-right:1px solid rgba(255,255,255,.25);gap:6px}
.stat:last-child{border-right:0}
.stat b{font-size:18px}
.stat span{font-size:12px}
.dots{position:absolute;display:flex;gap:6px}
.dots i{width:7px;height:7px;border-radius:50%;background:#ccc;display:block}
.dots i.on{background:#666}
/* sections */
.section-title{position:absolute;left:0;width:1200px;text-align:center;font-size:26px;font-weight:500}
.feature{position:absolute;width:320px;text-align:center}
.feature .icon{width:100px;height:100px;border-radius:50%;background:var(--navy);margin:0 auto 22px;display:flex;align-items:center;justify-content:center}
.feature h3{font-size:16px;font-weight:500;margin-bottom:4px;line-height:20px}
.feature p{font-size:12px;color:var(--muted);line-height:16px}
.feature .more{font-size:12px;color:var(--muted);margin-top:8px;display:inline-block}
.feature-hl{position:absolute;left:438px;top:1110px;width:324px;height:250px;background:var(--light)}
.destinations{position:absolute;left:0;top:1434px;width:1200px;height:698px;background:var(--navy)}
.view-more{position:absolute;right:80px;top:56px;color:var(--white);font-size:13px;text-decoration:underline}
.dest{position:absolute;width:247px}
.dest .ph{height:189px}
.dest p{color:var(--white);font-size:16px;font-weight:500;text-align:center;margin-top:16px}
.news-card{position:absolute;top:2259px;width:333px;height:330px;background:var(--light)}
.news-card .ph{position:absolute;left:10px;top:11px;width:313px;height:199px}
.news-card .date{position:absolute;left:10px;top:11px;width:34px;height:40px;background:var(--navy);color:var(--white);font-size:12px;text-align:center;line-height:15px;padding-top:5px}
.news-card .meta{position:absolute;left:20px;top:222px;right:20px;display:flex;justify-content:space-between;font-size:12px;color:var(--muted)}
.news-card .meta b{color:var(--ink);font-weight:500}
.news-card p{position:absolute;left:20px;right:20px;top:245px;font-size:12px;line-height:16px;color:var(--muted)}
.news-card .more{position:absolute;left:20px;top:282px;font-size:12px;color:var(--muted)}
.btn-navy{position:absolute;background:var(--navy);color:var(--white);border-radius:20px;font-size:13px;font-weight:500;display:flex;align-items:center;justify-content:center}
.partner{position:absolute;width:186px;height:130px;background:var(--light);display:flex;align-items:center;justify-content:center}
.partner i{display:block;width:96px;height:44px;background:#c9cfdc;border-radius:4px}
/* contact */
.contact{position:absolute;left:0;top:3160px;width:595px;height:435px;background:var(--navy)}
.contact h2{position:absolute;left:80px;top:80px;color:var(--white);font-size:24px;font-weight:500}
.field{position:absolute;background:var(--navy-dark);color:#e5e8f0;font-size:12px;padding:9px 12px;border:1px solid rgba(255,255,255,.08)}
.map{position:absolute;left:595px;top:3160px;width:605px;height:435px;background:linear-gradient(135deg,#e7e4dc,#d9dfd6 50%,#e8e4da)}
.map-card{position:absolute;left:685px;top:3252px;width:337px;height:99px;background:rgba(255,255,255,.92);font-size:12px;line-height:17px;padding:18px 20px 0 40px;color:var(--ink)}
/* footer */
.footer{position:absolute;left:0;top:3595px;width:1200px;height:329px;background:var(--footer);color:#ddd}
.footer h4{position:absolute;top:80px;font-size:16px;font-weight:500;color:var(--white)}
.footer ul{position:absolute;top:114px;list-style:disc;font-size:12px;line-height:19px;padding-left:14px}
.footer .txt{position:absolute;font-size:12px;line-height:19px}
.subscribe{position:absolute;left:892px;top:120px;width:228px;height:30px;background:var(--white);border-radius:15px;display:flex;align-items:center;justify-content:space-between;padding:0 4px 0 14px;font-size:11px;color:#555}
.subscribe b{background:var(--white);border:1px solid #333;border-radius:12px;padding:4px 10px;font-weight:400;color:#222}
.social{position:absolute;left:892px;top:170px;display:flex;gap:8px}
.social i{display:block;width:22px;height:22px;border-radius:50%;background:var(--white)}
.copy{position:absolute;left:0;top:3924px;width:1200px;height:58px;background:var(--navy);color:var(--white);font-size:12px;display:flex;align-items:center;justify-content:space-between;padding:0 80px}
</style>
</head>
<body>

<header class="topbar">
  <div class="brand"><span class="mark"></span>KORVALENDI</div>
  <div class="contact-item" style="left:590px">
    <svg width="26" height="26" viewBox="0 0 24 24" fill="none" stroke="#333" stroke-width="1.6"><path d="M5 3h4l2 5-3 2a12 12 0 0 0 6 6l2-3 5 2v4a2 2 0 0 1-2 2A17 17 0 0 1 3 5a2 2 0 0 1 2-2z"/></svg>
    <div><small>Call Us Now</small>(000) 000-0000</div>
  </div>
  <div class="contact-item" style="left:770px">
    <svg width="26" height="26" viewBox="0 0 24 24" fill="none" stroke="#333" stroke-width="1.6"><rect x="3" y="5" width="18" height="14" rx="2"/><path d="M3 7l9 6 9-6"/></svg>
    <div><small>Email Us Address</small>info@korvalendi.ae</div>
  </div>
  <div class="btn-apply">APPLY NOW</div>
</header>

<nav class="nav">
  <a class="active">Home</a><a>About Us</a><a>Why Study Abroad</a><a>Study Destinations</a><a>Our Services</a><a>Study English Language</a><a>Courses</a><a>Scholarships</a><a>Contact Us</a>
  <svg width="16" height="16" viewBox="0 0 24 24" fill="none" stroke="#fff" stroke-width="2" style="margin-left:8px"><circle cx="10" cy="10" r="7"/><path d="M15 15l6 6"/></svg>
</nav>

<section class="hero" role="img" aria-label="Smiling students holding books outside a university building">
  <div class="arrow" style="left:18px"><svg width="12" height="12" viewBox="0 0 12 12"><path d="M8 2L4 6l4 4" stroke="#333" stroke-width="2" fill="none"/></svg></div>
  <div class="arrow" style="left:1154px"><svg width="12" height="12" viewBox="0 0 12 12"><path d="M4 2l4 4-4 4" stroke="#333" stroke-width="2" fill="none"/></svg></div>
  <h1>KORVALENDI Is The Number One Choice<br>For Students To Study Abroad</h1>
  <div class="stats">
    <div class="stat"><svg width="30" height="26" viewBox="0 0 30 26" fill="#fff"><circle cx="8" cy="7" r="4"/><circle cx="22" cy="7" r="4"/><circle cx="15" cy="9" r="4.5"/><path d="M5 24c0-6 4-10 10-10s10 4 10 10z"/></svg><b>980+</b><span>Students</span></div>
    <div class="stat"><svg width="26" height="28" viewBox="0 0 26 28" fill="none" stroke="#fff" stroke-width="2"><rect x="3" y="2" width="20" height="24" rx="2"/><circle cx="13" cy="11" r="4"/><path d="M8 20h10"/></svg><b>150+</b><span>Immigration</span></div>
    <div class="stat"><svg width="30" height="28" viewBox="0 0 30 28" fill="#fff"><path d="M15 1l14 7H1z"/><rect x="4" y="10" width="3" height="12"/><rect x="11" y="10" width="3" height="12"/><rect x="17" y="10" width="3" height="12"/><rect x="23" y="10" width="3" height="12"/><rect x="1" y="24" width="28" height="3"/></svg><b>550+</b><span>Universities</span></div>
    <div class="stat"><svg width="28" height="28" viewBox="0 0 24 24" fill="none" stroke="#fff" stroke-width="1.8"><circle cx="12" cy="12" r="10"/><path d="M2 12h20M12 2c3 3 3 17 0 20M12 2c-3 3-3 17 0 20"/></svg><b>30+</b><span>Country</span></div>
  </div>
</section>
<div class="dots" style="left:579px;top:775px"><i class="on"></i><i></i><i></i><i></i></div>

<h2 class="section-title" style="top:804px">Why Korvalendi?</h2>
<div class="feature-hl"></div>

<div class="feature" style="left:60px;top:861px">
  <div class="icon"><svg width="46" height="46" viewBox="0 0 24 24" fill="none" stroke="#fff" stroke-width="1.4"><rect x="4" y="3" width="10" height="18"/><rect x="14" y="9" width="6" height="12"/><path d="M7 7h4M7 11h4M7 15h4M16 13h2M16 17h2"/></svg></div>
  <h3>Equipped Office</h3><p>Lorem Ipsum is simply dummy<br>of the printing and typesetting.</p><span class="more">Read More ⊕</span>
</div>
<div class="feature" style="left:440px;top:861px">
  <div class="icon"><svg width="46" height="46" viewBox="0 0 24 24" fill="none" stroke="#fff" stroke-width="1.4"><path d="M12 2l10 5H2z"/><path d="M5 9v9M9.5 9v9M14.5 9v9M19 9v9M2 21h20"/></svg></div>
  <h3>Official tie up with Universities,<br>Institutions, and Schools</h3><p>Lorem Ipsum is simply dummy<br>of the printing and typesetting.</p><span class="more">Read More ⊕</span>
</div>
<div class="feature" style="left:820px;top:861px">
  <div class="icon"><svg width="46" height="46" viewBox="0 0 24 24" fill="none" stroke="#fff" stroke-width="1.4"><circle cx="12" cy="8" r="4"/><path d="M4 21c0-5 4-8 8-8s8 3 8 8"/></svg></div>
  <h3>Experienced Counselors</h3><p>Lorem Ipsum is simply dummy<br>of the printing and typesetting.</p><span class="more">Read More ⊕</span>
</div>
<div class="feature" style="left:60px;top:1134px">
  <div class="icon"><svg width="46" height="46" viewBox="0 0 24 24" fill="none" stroke="#fff" stroke-width="1.4"><path d="M12 2l8 3v6c0 5-4 9-8 11-4-2-8-6-8-11V5z"/><path d="M8 12l3 3 5-6"/></svg></div>
  <h3>Quality of Counseling</h3><p>Lorem Ipsum is simply dummy<br>of the printing and typesetting.</p><span class="more">Read More ⊕</span>
</div>
<div class="feature" style="left:440px;top:1134px">
  <div class="icon"><svg width="46" height="46" viewBox="0 0 24 24" fill="none" stroke="#fff" stroke-width="1.4"><rect x="4" y="3" width="13" height="18"/><path d="M7 7h7M7 11h7M7 15h4M20 8l-6 9-2 1 1-2 6-9z"/></svg></div>
  <h3>Registration / License</h3><p>Lorem Ipsum is simply dummy<br>of the printing and typesetting.</p><span class="more">Read More ⊕</span>
</div>
<div class="feature" style="left:820px;top:1134px">
  <div class="icon"><svg width="46" height="46" viewBox="0 0 24 24" fill="none" stroke="#fff" stroke-width="1.4"><circle cx="12" cy="12" r="10"/><path d="M2 12h20M12 2c3 3 3 17 0 20M12 2c-3 3-3 17 0 20M4 7h16M4 17h16"/></svg></div>
  <h3>Range of Countries</h3><p>Lorem Ipsum is simply dummy<br>of the printing and typesetting.</p><span class="more">Read More ⊕</span>
</div>

<section class="destinations">
  <h2 class="section-title" style="top:42px;color:#fff">Study Destinations</h2>
  <span class="view-more">View More</span>
  <div class="dest" style="left:80px;top:103px"><div class="ph" role="img" aria-label="Student in front of a United Kingdom flag" style="background:linear-gradient(135deg,#8c3a45,#c9c2c4 50%,#34407a)"></div><p>Study in UK</p></div>
  <div class="dest" style="left:345px;top:103px"><div class="ph" role="img" aria-label="Students holding a United States flag" style="background:linear-gradient(135deg,#c8d4de,#b9454c 55%,#3a4678)"></div><p>Study in USA</p></div>
  <div class="dest" style="left:611px;top:103px"><div class="ph" role="img" aria-label="Student studying Australia book" style="background:linear-gradient(135deg,#3d5aa1,#c49a86 55%,#7b4d3f)"></div><p>Study in Australia</p></div>
  <div class="dest" style="left:876px;top:103px"><div class="ph" role="img" aria-label="Speech sign asking about speaking English" style="background:linear-gradient(135deg,#b2373d,#e9e4dc 50%,#7f7a76)"></div><p>Study English Language</p></div>
  <div class="dest" style="left:80px;top:369px"><div class="ph" role="img" aria-label="Student in front of a New Zealand flag" style="background:linear-gradient(135deg,#2d3a75,#9b3c4a 45%,#ad8f78)"></div><p>Study in New Zealand</p></div>
  <div class="dest" style="left:345px;top:369px"><div class="ph" role="img" aria-label="Reader near a European landmark tower" style="background:linear-gradient(135deg,#d9dde1,#a9b0b8 55%,#c98f8a)"></div><p>Study in Europe</p></div>
  <div class="dest" style="left:611px;top:369px"><div class="ph" role="img" aria-label="Student reading in a library" style="background:linear-gradient(135deg,#4d3a2c,#a07a52 50%,#3d3c48)"></div><p>Study in Malaysia</p></div>
  <div class="dest" style="left:876px;top:369px"><div class="ph" role="img" aria-label="Students with notebooks in a classroom" style="background:linear-gradient(135deg,#e6e6e6,#b8c2cc 55%,#9aa46a)"></div><p>Study in UAE</p></div>
</section>

<h2 class="section-title" style="top:2188px">News &amp; Updates</h2>
<article class="news-card" style="left:80px"><div class="ph" role="img" aria-label="Group of happy students outdoors" style="background:linear-gradient(135deg,#8aa27a,#c9a48a 50%,#5f6d52)"></div><div class="date">19<br>Oct</div><div class="meta"><b>POST TITLE</b><span>▦ October 18, 2018</span></div><p>Lorem Ipsum is simply in dummy text the printing in matter and typesetting industry.</p><span class="more">Read More.. ⊕</span></article>
<article class="news-card" style="left:433px"><div class="ph" role="img" aria-label="Student holding books between library shelves" style="background:linear-gradient(135deg,#5a4a3a,#a08066 50%,#3b4256)"></div><div class="date">19<br>Oct</div><div class="meta"><b>POST TITLE</b><span>▦ October 18, 2018</span></div><p>Lorem Ipsum is simply in dummy text the printing in matter and typesetting industry.</p><span class="more">Read More.. ⊕</span></article>
<article class="news-card" style="left:788px"><div class="ph" role="img" aria-label="Students walking through a university corridor" style="background:linear-gradient(135deg,#cfcfcf,#8e8e8e 50%,#e0e0e0)"></div><div class="date">19<br>Oct</div><div class="meta"><b>POST TITLE</b><span>▦ October 18, 2018</span></div><p>Lorem Ipsum is simply in dummy text the printing in matter and typesetting industry.</p><span class="more">Read More.. ⊕</span></article>
<div class="btn-navy" style="left:520px;top:2623px;width:168px;height:40px">Read More</div>

<h2 class="section-title" style="top:2719px">Our Partners</h2>
<div class="partner" style="left:80px;top:2782px"><i></i></div>
<div class="partner" style="left:293px;top:2782px"><i></i></div>
<div class="partner" style="left:507px;top:2782px"><i></i></div>
<div class="partner" style="left:720px;top:2782px"><i></i></div>
<div class="partner" style="left:934px;top:2782px"><i></i></div>
<div class="partner" style="left:80px;top:2935px"><i></i></div>
<div class="partner" style="left:293px;top:2935px"><i></i></div>
<div class="partner" style="left:507px;top:2935px"><i></i></div>
<div class="partner" style="left:720px;top:2935px"><i></i></div>
<div class="partner" style="left:934px;top:2935px"><i></i></div>
<div class="dots" style="left:589px;top:3093px"><i class="on"></i><i></i><i></i></div>

<section class="contact">
  <h2>Quick Contact</h2>
  <div class="field" style="left:80px;top:132px;width:225px;height:35px">First Name</div>
  <div class="field" style="left:324px;top:132px;width:215px;height:35px">Last Name</div>
  <div class="field" style="left:80px;top:175px;width:225px;height:35px">Email</div>
  <div class="field" style="left:324px;top:175px;width:215px;height:35px">Phone</div>
  <div class="field" style="left:80px;top:223px;width:459px;height:100px">Message</div>
  <div class="btn-navy" style="left:80px;top:342px;width:167px;height:38px;background:#fff;color:#222">View All</div>
</section>
<div class="map" role="img" aria-label="Street map showing the office location"></div>
<svg class="abs" style="left:738px;top:3196px" width="26" height="36" viewBox="0 0 26 36"><path d="M13 0C6 0 0 6 0 13c0 9 13 23 13 23s13-14 13-23C26 6 20 0 13 0z" fill="#e0483a"/><circle cx="13" cy="13" r="5" fill="#fff"/></svg>
<div class="map-card">
  <svg class="abs" style="left:16px;top:20px" width="12" height="14" viewBox="0 0 12 16"><path d="M6 0a6 6 0 0 0-6 6c0 4 6 10 6 10s6-6 6-10a6 6 0 0 0-6-6z" fill="#333"/></svg>
  48 Harbour Lane, Westbrook<br>USA Zip 5120<br>+100 222 3344
</div>

<footer class="footer">
  <div class="brand" style="left:66px;top:62px;color:#fff"><span class="mark" style="background:#fff"></span>KORVALENDI</div>
  <div class="txt" style="left:66px;top:130px;width:210px">Lorem Ipsum is simply dummy text of the printing and typese tting industry.</div>
  <div class="txt" style="left:66px;top:200px">READ MORE.. ⊕</div>
  <h4 style="left:332px">Quick Link</h4>
  <ul style="left:332px"><li>Study in UK</li><li>Study in USA</li><li>Study in Australia</li><li>Study in New Zealand</li><li>Study in Europe</li><li>Study in Malaysia</li><li>Study in UAE</li></ul>
  <h4 style="left:566px">Quick Contact</h4>
  <div class="txt" style="left:566px;top:114px;width:250px">◉ Palm Crescent Tower, office 31,<br>&nbsp;&nbsp;&nbsp;&nbsp;3rd floor,<br>&nbsp;&nbsp;&nbsp;&nbsp;po box - 4410<br>✆ +971 50 000 4821<br>✉ info@korvalendi.ae</div>
  <h4 style="left:892px">Subscribe</h4>
  <div class="txt" style="left:892px;top:100px;font-size:11px">Subscribe For Our Newsletter</div>
  <div class="subscribe">Email Address<b>Subscribe</b></div>
  <div class="social"><i></i><i></i><i></i><i></i></div>
</footer>
<div class="copy"><span>CopyRight © 2018 KORVALENDI . All Right Reserve</span><span>Privacy Policy - Terms &amp; Conditions</span></div>

</body>
</html>
```